Career Management Consultant Fun Professional Business Card

This is a business card for a personal career management consultant. The vibe needs to be professional but fun, modern with colour.

The name of the business is "Marcus Telvorne Career Management Consulting"

The name of the individual is "Marcus Telvorne" and his title is "Career Management Consultant"

Contact Information for Business Card

Marcus Telvorne
Phone: 0400 731 862
Email: Marcus.Telvorne@quillmail.net

```html
<!DOCTYPE html>
<html lang="en">
<head>
<meta charset="utf-8">
<title>Marcus Telvorne – Business Card</title>
<link href="https://fonts.googleapis.com/css2?family=Dosis:wght@300;400;600&display=swap" rel="stylesheet">
<style>
  :root {
    --backdrop: #e4e4e4;
    --card-dark: #0b0b0b;
    --card-light: #f1f1f1;
    --ink-light: #ffffff;
    --ink-dark: #2a2a2a;
    --ink-mid: #555555;
    --ink-faint: #d2d2d2;
    --accent: #1fb5a8;
    --accent-warm: #f26b4f;
  }
  * { box-sizing: border-box; margin: 0; padding: 0; }
  html, body {
    width: 1200px;
    height: 1200px;
    overflow: hidden;
    background: var(--backdrop);
    font-family: "Dosis", sans-serif;
  }
  .sheet {
    position: relative;
    width: 1200px;
    height: 1200px;
  }
  .card {
    position: absolute;
    left: 160px;
    width: 880px;
    height: 503px;
    overflow: hidden;
    box-shadow: 0 18px 40px rgba(0, 0, 0, 0.18);
  }
  .card--front { top: 75px; background: var(--card-dark); color: var(--ink-light); }
  .card--back { top: 622px; background: var(--card-light); color: var(--ink-dark); }

  .card__band {
    position: absolute;
    left: 0;
    bottom: 0;
    width: 100%;
    height: 10px;
    background: linear-gradient(90deg, var(--accent), var(--accent-warm));
  }
  .card--back .card__band { top: 0; bottom: auto; }

  /* wordmark */
  .wordmark {
    display: flex;
    align-items: center;
    gap: 14px;
    font-weight: 600;
    letter-spacing: 0.02em;
    white-space: nowrap;
  }
  .wordmark__dot {
    width: 22px;
    height: 22px;
    border-radius: 50%;
    border: 5px solid var(--accent);
    flex: none;
  }

  /* front */
  .front__lockup {
    position: absolute;
    left: 50%;
    top: 50%;
    transform: translate(-50%, -50%);
    display: flex;
    align-items: center;
    gap: 40px;
  }
  .front__lockup .wordmark { font-size: 34px; }
  .front__divider { width: 2px; height: 80px; background: var(--accent); flex: none; }
  .front__text { white-space: nowrap; }
  .front__name { font-size: 30px; font-weight: 600; line-height: 1.2; }
  .front__company { font-size: 26px; font-weight: 300; line-height: 1.2; }

  /* back */
  .back__brand {
    position: absolute;
    left: 60px;
    top: 150px;
    white-space: nowrap;
  }
  .back__brand .wordmark { font-size: 38px; color: var(--ink-dark); margin-bottom: 34px; }
  .back__name { font-size: 27px; font-weight: 600; line-height: 1.2; }
  .back__company { font-size: 24px; font-weight: 400; line-height: 1.2; color: var(--ink-dark); }

  .back__decor {
    position: absolute;
    right: 40px;
    top: 160px;
    display: flex;
    align-items: center;
    gap: 20px;
    color: var(--ink-faint);
    font-size: 90px;
    font-weight: 600;
    line-height: 1;
    white-space: nowrap;
  }
  .back__decor .wordmark__dot {
    width: 68px;
    height: 68px;
    border-width: 15px;
    border-color: var(--ink-faint);
  }

  .back__person {
    position: absolute;
    right: 50px;
    top: 42px;
    text-align: right;
    white-space: nowrap;
  }
  .back__person-name { font-size: 28px; font-weight: 400; color: var(--ink-mid); line-height: 1.2; }
  .back__person-role { font-size: 18px; font-weight: 400; color: var(--accent); line-height: 1.3; }

  .back__contact {
    position: absolute;
    left: 470px;
    bottom: 60px;
    list-style: none;
    font-size: 22px;
    color: var(--ink-mid);
    white-space: nowrap;
  }
  .back__contact li { display: flex; align-items: center; gap: 12px; line-height: 1.6; }
  .back__contact svg { width: 18px; height: 18px; fill: var(--accent); flex: none; }
</style>
</head>
<body>
<main class="sheet">

  <section class="card card--front" aria-label="Card front">
    <div class="front__lockup">
      <div class="wordmark"><span class="wordmark__dot"></span>Telvorne</div>
      <div class="front__divider"></div>
      <div class="front__text">
        <p class="front__name">Marcus Telvorne</p>
        <p class="front__company">Career Management Consulting</p>
      </div>
    </div>
    <div class="card__band"></div>
  </section>

  <section class="card card--back" aria-label="Card back">
    <div class="card__band"></div>

    <div class="back__decor" aria-hidden="true">
      <span class="wordmark__dot"></span>Telvorne
    </div>

    <div class="back__brand">
      <div class="wordmark"><span class="wordmark__dot"></span>Telvorne</div>
      <p class="back__name">Marcus Telvorne</p>
      <p class="back__company">Career Management Consulting</p>
    </div>

    <div class="back__person">
      <p class="back__person-name">Marcus Telvorne</p>
      <p class="back__person-role">Career Management Consultant</p>
    </div>

    <ul class="back__contact">
      <li>
        <svg viewBox="0 0 16 16" aria-hidden="true"><path d="M4 1h8a1 1 0 0 1 1 1v12a1 1 0 0 1-1 1H4a1 1 0 0 1-1-1V2a1 1 0 0 1 1-1zm1 2v8h6V3H5zm3 9.2a.9.9 0 1 0 0 1.8.9.9 0 0 0 0-1.8z"/></svg>
        0400 731 862
      </li>
      <li>
        <svg viewBox="0 0 16 16" aria-hidden="true"><path d="M1 3h14v10H1V3zm1.5 1.5v.3L8 8.6l5.5-3.8v-.3h-11zm11 1.9L8 10.2 2.5 6.4v5.1h11V6.4z"/></svg>
        Marcus.Telvorne@quillmail.net
      </li>
    </ul>
  </section>

</main>
</body>
</html>
```